RTW Vision and Core Values

We are wanting to promote our core values and vision on posters at our office. I have uploaded a copy of our logo. We would like to incorporate that, the vision and the core values. ALL THREE MUST BE INCLUDED ON THE DESIGN. For reference, our website is www.rtwpetroworks.com

Our vision is:
We are a Team of Power and Strength that Builds our People and Serves our Industry and Communities.

Our Values are:
We Operate with a Standard of Excellence.
We Do the Right Thing Every Time.
We Value and Recognize our People.
We are Team Players.
We Think and Act with Optimism and Faith.

```html
<!DOCTYPE html>
<html lang="en">
<head>
<meta charset="utf-8">
<title>RTW Vision and Core Values</title>
<link href="https://fonts.googleapis.com/css2?family=Barlow:wght@600;700;800&display=swap" rel="stylesheet">
<style>
  :root {
    --ink: #161616;
    --brand-blue: #1f3fc4;
    --royal: #2f6af7;
    --deep: #0a1ca8;
    --ring: #1b4a66;
    --gold-top: #f9ad0c; --gold-bot: #ec9606;
    --violet-top: #3c4ff4; --violet-bot: #1418e4;
    --navy-top: #1a5ccb; --navy-bot: #0e4595;
    --amber-top: #fd8a1c; --amber-bot: #f26807;
    --rose-top: #ff2b7c; --rose-bot: #c8187c;
    --white: #ffffff;
  }
  * { box-sizing: border-box; margin: 0; padding: 0; }
  html, body { width: 813px; height: 1200px; overflow: hidden; background: #fff; }
  body { font-family: "Barlow", Arial, sans-serif; }
  .poster { position: relative; width: 813px; height: 1200px; background: var(--white); overflow: hidden; }
  .backdrop { position: absolute; inset: 0; width: 813px; height: 1200px; }
  .brand-badge {
    position: absolute; left: 585px; top: 44px; width: 160px; height: 160px; border-radius: 50%;
    background: radial-gradient(circle at 40% 35%, #ffffff 55%, #e6e8ec);
    box-shadow: 0 2px 6px rgba(0,0,0,.15);
    display: flex; align-items: center; justify-content: center;
  }
  .brand-name { font-weight: 800; color: var(--brand-blue); font-size: 46px; letter-spacing: 2px; }
  .welcome {
    position: absolute; left: 45px; top: 217px; font-size: 64px; font-weight: 800;
    color: var(--ink); line-height: 1;
  }
  .welcome-rule { position: absolute; left: 45px; top: 290px; width: 192px; height: 4px; background: var(--royal); border-radius: 2px; }
  .vision {
    position: absolute; left: 45px; top: 362px; font-size: 27px; font-weight: 600;
    color: var(--ink); line-height: 36px; white-space: nowrap;
  }
  .hub {
    position: absolute; left: 310px; top: 585px; width: 196px; height: 196px; border-radius: 50%;
    background: var(--ring); box-shadow: 2px 4px 8px rgba(0,0,0,.25);
  }
  .hub::before { content: ""; position: absolute; inset: 12px; border-radius: 50%; background: var(--white); }
  .hub-core {
    position: absolute; inset: 19px; border-radius: 50%; border: 7px solid var(--ring); background: var(--white);
    display: flex; align-items: center; justify-content: center;
  }
  .hub-core .brand-name { font-size: 40px; }
  .value {
    position: absolute; border-radius: 80px; display: flex; align-items: center;
    color: var(--white); font-weight: 700; font-size: 24px; line-height: 33px; letter-spacing: .3px;
    white-space: nowrap; box-shadow: 3px 4px 6px rgba(0,0,0,.2);
  }
  .value-icon {
    position: absolute; top: 50%; transform: translateY(-50%);
    width: 72px; height: 72px; border-radius: 50%; border: 4px solid rgba(255,255,255,.35);
    background: radial-gradient(circle, #ffffff 55%, #dfe6ef);
  }
  .value--optimism { left: 10px; top: 524px; width: 303px; height: 149px; padding-left: 93px; background: linear-gradient(var(--gold-top) 48%, var(--gold-bot) 48%); }
  .value--optimism .value-icon { left: 12px; }
  .value--excellence { left: 499px; top: 525px; width: 301px; height: 149px; padding-left: 98px; background: linear-gradient(var(--violet-top) 48%, var(--violet-bot) 48%); }
  .value--excellence .value-icon { left: 12px; }
  .value--team { left: 29px; top: 776px; width: 314px; height: 158px; padding-left: 98px; background: linear-gradient(var(--navy-top) 50%, var(--navy-bot) 50%); }
  .value--team .value-icon { left: 12px; }
  .value--right { left: 466px; top: 776px; width: 319px; height: 158px; padding-left: 97px; background: linear-gradient(var(--amber-top) 48%, var(--amber-bot) 48%); }
  .value--right .value-icon { left: 10px; }
  .value--people { left: 252px; top: 949px; width: 313px; height: 157px; padding-left: 106px; background: linear-gradient(var(--rose-top) 48%, var(--rose-bot) 48%); }
  .value--people .value-icon { left: 13px; }
</style>
</head>
<body>
<main class="poster">
  <svg class="backdrop" viewBox="0 0 853 1104" preserveAspectRatio="none" aria-hidden="true">
    <defs>
      <linearGradient id="header-sweep" x1="0" y1="0" x2="1" y2="0">
        <stop offset="0" stop-color="#2f62f8"/>
        <stop offset="0.6" stop-color="#3d86f8"/>
        <stop offset="1" stop-color="#52c2fb"/>
      </linearGradient>
      <linearGradient id="header-block" x1="0" y1="0" x2="1" y2="0">
        <stop offset="0" stop-color="#2f5ff5"/>
        <stop offset="1" stop-color="#4db8fb"/>
      </linearGradient>
    </defs>
    <polygon points="0,0 853,0 853,321 0,97" fill="url(#header-sweep)"/>
    <polygon points="531,177 853,247 853,321 531,237" fill="url(#header-block)"/>
    <polygon points="433,192 660,252 660,287 433,227" fill="var(--deep)"/>
    <g fill="none" stroke-width="6">
      <polyline points="326,553 380,553" stroke="var(--gold-top)" vector-effect="non-scaling-stroke"/>
      <polyline points="476,553 528,553" stroke="var(--violet-bot)" vector-effect="non-scaling-stroke"/>
      <polyline points="416,720 416,793 355,793" stroke="var(--navy-top)" vector-effect="non-scaling-stroke"/>
      <polyline points="440,720 440,793 495,793" stroke="var(--amber-bot)" vector-effect="non-scaling-stroke"/>
      <polyline points="428,720 428,876" stroke="var(--rose-top)" vector-effect="non-scaling-stroke"/>
    </g>
  </svg>

  <div class="brand-badge"><span class="brand-name">RTW</span></div>

  <h1 class="welcome">WELCOME</h1>
  <div class="welcome-rule"></div>
  <p class="vision">We are a Team of Power and Strength that Builds our People<br>and Serves our Industry and Communities.</p>

  <div class="hub"><div class="hub-core"><span class="brand-name">RTW</span></div></div>

  <div class="value value--optimism">
    <div class="value-icon" role="img" aria-label="Illustration of a person surrounded by colourful idea icons"></div>
    <span class="value-text">We Think and Act<br>with Optimism<br>and Faith</span>
  </div>
  <div class="value value--excellence">
    <div class="value-icon" role="img" aria-label="Illustration of an award rosette with stars"></div>
    <span class="value-text">We Operate with<br>a Standard of<br>Excellence</span>
  </div>
  <div class="value value--team">
    <div class="value-icon" role="img" aria-label="Illustration of a group of colleagues"></div>
    <span class="value-text">We are Team<br>Players</span>
  </div>
  <div class="value value--right">
    <div class="value-icon" role="img" aria-label="Illustration of a person pushing toward a goal"></div>
    <span class="value-text">We Do the Right<br>Thing Every<br>Time</span>
  </div>
  <div class="value value--people">
    <div class="value-icon" role="img" aria-label="Illustration of a group of people"></div>
    <span class="value-text">We Value and<br>Recognize our<br>People</span>
  </div>
</main>
</body>
</html>
```